Supplement Bottle Packaging and Design

We want to rebrand our current health supplements (see below). We do want it to be modern, vibrant and appealing supplement bottles. Very upscale and elegant as it targets primarily women.
NOTE: READ THE ATTACHED WORD DOCUMENT!
Bottle size: We are totally open to the bottle size and shape, as long it's a typical supplement bottle size to handle 90-120 capsules; what we mostly need is new bottle design/packaging. YOU DON’T HAVE TO USE THE CURRENT WHITE BOTTLE SHAPE, BUT ANYTHING MORE MODERN WOULD WORK!
Updates
We need more modern, clean sleek designs to choose from
Look and feel
Each slider illustrates characteristics of the customer's brand and the style your logo design should communicate.

```html
<!DOCTYPE html>
<html lang="en">
<head>
<meta charset="utf-8">
<title>Align Supplement Labels</title>
<link href="https://fonts.googleapis.com/css2?family=Exo:wght@500;600;700&family=Lato:wght@400;700&display=swap" rel="stylesheet">
<style>
  :root {
    --bg: #ebebed;
    --ink: #ffffff;
    --pill-ink: #1e1e22;
    --liver-a: #9c4579; --liver-b: #c95f9e; --liver-title: #f58fc0; --liver-pill: #cd5ea0;
    --tummy-a: #ab2228; --tummy-b: #da2828; --tummy-title: #f0646a; --tummy-pill: #ef5a5a;
    --hormone-a: #1c3f35; --hormone-b: #3b5f56; --hormone-title: #5fa597; --hormone-pill: #62a99b;
    --sugar-a: #3a3f8f; --sugar-b: #5779c6; --sugar-title: #5f84d6; --sugar-pill: #6c90d0;
  }
  * { margin: 0; padding: 0; box-sizing: border-box; }
  html, body { width: 1200px; height: 1005px; overflow: hidden; }
  body { background: var(--bg); position: relative; font-family: "Exo", sans-serif; }

  .label-sheet {
    position: absolute; left: 45px; top: 336px;
    display: flex; gap: 30px;
  }

  .label {
    position: relative; width: 255px; height: 332px;
    overflow: hidden; color: var(--ink);
    background: linear-gradient(215deg, var(--b) 0%, var(--a) 100%);
  }
  .label--liver   { --a: var(--liver-a);   --b: var(--liver-b);   --t: var(--liver-title);   --p: var(--liver-pill); }
  .label--tummy   { --a: var(--tummy-a);   --b: var(--tummy-b);   --t: var(--tummy-title);   --p: var(--tummy-pill); }
  .label--hormone { --a: var(--hormone-a); --b: var(--hormone-b); --t: var(--hormone-title); --p: var(--hormone-pill); }
  .label--sugar   { --a: var(--sugar-a);   --b: var(--sugar-b);   --t: var(--sugar-title);   --p: var(--sugar-pill); }

  .motif-area {
    position: absolute; left: 150px; top: 100px; width: 105px; height: 200px;
    background: radial-gradient(ellipse at 100% 50%, rgba(255,255,255,0.22) 0%, rgba(255,255,255,0.08) 55%, rgba(255,255,255,0) 75%);
  }

  .product-name {
    position: absolute; left: 14px; top: 31px;
    font-weight: 600; font-size: 43px; line-height: 35px; letter-spacing: -0.6px;
  }
  .product-name .focus-area { display: block; color: var(--t); }
  .product-name .line-name { display: block; color: var(--ink); }

  .claim {
    position: absolute; left: 18px; top: 123px;
    font-weight: 500; font-size: 15px; line-height: 19px; letter-spacing: 0.2px;
  }
  .label--sugar .claim { top: 160px; }

  .count-pill {
    position: absolute; left: 0; top: 254px; width: 169px; height: 62px;
    background: var(--p); border-radius: 0 31px 31px 0;
    font-family: "Lato", sans-serif; color: var(--pill-ink);
    font-size: 12px; line-height: 17px; padding: 13px 0 0 22px;
  }
  .count-pill .count { display: block; margin-left: -1px; }
</style>
</head>
<body>

<main class="label-sheet">
  <section class="label label--liver">
    <div class="motif-area" role="img" aria-label="Decorative line motif"></div>
    <h2 class="product-name"><span class="focus-area">LIVER</span><span class="line-name">ALIGN</span></h2>
    <p class="claim">Rejuvenating<br>Cleanse &amp; Detox<br>Formula*</p>
    <div class="count-pill">Dietary Supplement<span class="count">120 Vegetable Capsules</span></div>
  </section>

  <section class="label label--tummy">
    <div class="motif-area" role="img" aria-label="Decorative line motif"></div>
    <h2 class="product-name"><span class="focus-area">TUMMY</span><span class="line-name">ALIGN</span></h2>
    <p class="claim">Oxygenating<br>Colon Cleanse*</p>
    <div class="count-pill">Dietary Supplement<span class="count">90 Vegetable Capsules</span></div>
  </section>

  <section class="label label--hormone">
    <div class="motif-area" role="img" aria-label="Decorative line motif"></div>
    <h2 class="product-name"><span class="focus-area">HORMONE</span><span class="line-name">ALIGN</span></h2>
    <p class="claim">Supports Healthy<br>Hormone Levels*</p>
    <div class="count-pill">Dietary Supplement<span class="count">60 Vegetable Capsules</span></div>
  </section>

  <section class="label label--sugar">
    <div class="motif-area" role="img" aria-label="Decorative line motif"></div>
    <h2 class="product-name"><span class="focus-area">BLOOD</span><span class="focus-area">SUGAR</span><span class="line-name">ALIGN</span></h2>
    <p class="claim">Supports Healthy<br>Blood Glucose<br>Levels*</p>
    <div class="count-pill">Dietary Supplement<span class="count">60 Vegetable Capsules</span></div>
  </section>
</main>

</body>
</html>
```